Steady Yield Fund

Need to design a h: 200 w: 260mm advert for print publishing. The product is an investment fund that pays monthly cash distributions.

Background on product:
https://tarnwellcapital.com.au/our-funds/steady-yield-smallcap-fund/

NEWSPRINT TECHNICAL SPECIFICATIONS
The following are print specifications to assist the preparation and creation of PDF artwork files for Newsprint advertising for the above mentioned publications.

Image Resolution
We print at a linescreen ruling of 100 lpi. Please supply at a minimum of:

Images: 150 dpi
Single bitmap: 600 dpi
Logos supplied as either single bitmap or vector artwork.

Colour
Colour should be supplied as CMYK.

Total Ink Coverage
Ensure all elements including TIFFs, JPEGs, or EPS images do not exceed (CMYK) 240% total ink.

Fonts and Type
It is not recommend reversing text out of four colour images. Minimum type sizes are:

Single solid colour: 6 pt
Coloured type on a white background using two or three colour plates: 8 pt
Reversed type out of one colour plates: 8 pt
Reversed type out of two or more colour plates: 12 pt san serif, bold

```html
<!DOCTYPE html>
<html lang="en">
<head>
<meta charset="utf-8">
<title>Steady Yield Value Smallcap Fund – Tarnwell Capital</title>
<link rel="stylesheet" href="https://fonts.googleapis.com/css2?family=Poppins:wght@300;700&display=swap">
<style>
  :root {
    --bg-mid: #474747;
    --bg-band: #1a1a1a;
    --portrait-light: #3a3a3a;
    --portrait-dark: #232323;
    --gold: #d4a54c;
    --white: #ffffff;
  }
  html, body {
    margin: 0;
    padding: 0;
    width: 1200px;
    height: 923px;
    overflow: hidden;
    background: var(--bg-mid);
  }
  .advert {
    position: relative;
    width: 1200px;
    height: 923px;
    overflow: hidden;
    font-family: "Poppins", sans-serif;
  }
  .advert__scene {
    position: absolute;
    inset: 0;
    background:
      linear-gradient(180deg, rgba(26,26,26,0) 22%, rgba(26,26,26,0.75) 36%, rgba(26,26,26,0.8) 52%, rgba(26,26,26,0) 64%),
      linear-gradient(90deg, #404040 0%, var(--bg-mid) 100%);
  }
  .advert__portrait {
    position: absolute;
    left: 505px;
    top: 56px;
    right: 0;
    bottom: 0;
    border-radius: 340px 0 0 0;
    background: linear-gradient(160deg, var(--portrait-light) 0%, var(--portrait-dark) 60%, #1f1f1f 100%);
  }
  .brand {
    position: absolute;
    left: 83px;
    top: 88px;
    margin: 0;
    color: var(--gold);
    font-weight: 700;
    font-size: 62px;
    line-height: 68px;
    letter-spacing: -0.5px;
  }
  .headline {
    position: absolute;
    left: 87px;
    top: 580px;
    margin: 0;
    color: var(--white);
    font-weight: 700;
    font-size: 73px;
    line-height: 80px;
    letter-spacing: -0.3px;
  }
  .tagline {
    position: absolute;
    left: 86px;
    top: 747px;
    margin: 0;
    color: var(--gold);
    font-weight: 300;
    font-size: 39px;
    line-height: 51px;
  }
</style>
</head>
<body>
  <main class="advert">
    <div class="advert__scene" role="img" aria-label="Softly blurred black and white office interior in the background"></div>
    <div class="advert__portrait" role="img" aria-label="Black and white photograph of a smiling businessman in a dark suit and tie with arms crossed"></div>
    <p class="brand">Tarnwell<br>Capital</p>
    <h1 class="headline">Steady Yield Value<br>Smallcap Fund</h1>
    <p class="tagline">For wholesale investors looking<br>for regular cash income</p>
  </main>
</body>
</html>
```